Lawn care & general maintenance

I need a business card desisign for a new business in north bay called The Hedge Buddy i offer services like lawn care, snow removal, and general maintenance such as dry walling painting, brush removal, and other little maintenance work.

The font must be like the font on my work hate

Industry/Entity Type

Business

Contact Information for Business Card

Derek Ossington, Company name: The Hedge Buddy

Logo Text

The Hedge Buddy- in jetson print

Logo styles of interest
Pictorial/Combination Logo
Requirements
Must have
• Slogan: We mow down the toughest jobs, just ask!

```html
<!DOCTYPE html>
<html lang="en">
<head>
<meta charset="utf-8">
<title>The Hedge Buddy – Business Card</title>
<link rel="stylesheet" href="https://fonts.googleapis.com/css2?family=Montserrat:wght@500;700&family=Righteous&display=swap">
<style>
  :root {
    --grass-light: #b4cf7a;
    --grass-mid: #86ad4f;
    --grass-deep: #4f7a2c;
    --brand-green: #4a7c36;
    --panel: #f2f2f3;
    --ink: #2b2d31;
    --white: #ffffff;
  }
  html, body {
    margin: 0;
    width: 1200px;
    height: 741px;
    overflow: hidden;
    background: #ffffff;
  }
  .card {
    position: relative;
    width: 1200px;
    height: 741px;
    overflow: hidden;
    font-family: "Montserrat", sans-serif;
  }
  .card__backdrop {
    position: absolute;
    inset: 0;
    background:
      radial-gradient(ellipse at 25% 20%, var(--grass-light) 0%, transparent 55%),
      radial-gradient(ellipse at 80% 85%, var(--grass-mid) 0%, transparent 60%),
      linear-gradient(160deg, #9fc064 0%, var(--grass-mid) 50%, var(--grass-deep) 100%);
  }
  .card__shapes {
    position: absolute;
    inset: 0;
  }
  .brand {
    position: absolute;
    left: 92px;
    top: 166px;
  }
  .brand__name {
    margin: 0;
    font-family: "Montserrat", sans-serif;
    font-weight: 700;
    font-size: 24px;
    line-height: 1.2;
    color: var(--ink);
    white-space: nowrap;
  }
  .brand__slogan {
    margin: 8px 0 0;
    font-weight: 500;
    font-size: 14px;
    line-height: 1.3;
    color: var(--white);
    white-space: nowrap;
  }
  .label {
    position: absolute;
    right: 737px;
    margin: 0;
    font-family: "Righteous", sans-serif;
    font-size: 35px;
    color: var(--ink);
    line-height: 1;
  }
  .value {
    position: absolute;
    margin: 0;
    font-weight: 700;
    line-height: 1;
    letter-spacing: 1px;
  }
  .value--on-green { color: var(--white); font-size: 36px; }
  .value--on-white { color: var(--brand-green); font-size: 36px; }
  .value--web { color: var(--brand-green); font-size: 27px; letter-spacing: 0.5px; }
</style>
</head>
<body>
<main class="card">
  <div class="card__backdrop" role="img" aria-label="Close-up photograph of fresh green grass blades"></div>

  <svg class="card__shapes" width="1200" height="741" viewBox="0 0 1200 741" aria-hidden="true">
    <path d="M254 348 H540 V638 H254 A43 43 0 0 1 211 595 V391 A43 43 0 0 1 254 348 Z" fill="var(--panel)"/>
    <rect x="530" y="348" width="560" height="71" fill="var(--brand-green)"/>
    <rect x="521" y="419" width="560" height="74" fill="var(--panel)"/>
    <rect x="510" y="493" width="562" height="72" fill="var(--brand-green)"/>
    <rect x="504" y="565" width="553" height="73" fill="var(--panel)"/>
    <line x1="537" y1="303" x2="489" y2="683" stroke="var(--ink)" stroke-width="11"/>
  </svg>

  <header class="brand">
    <h1 class="brand__name">The Hedge Buddy</h1>
    <p class="brand__slogan">We mow down the toughest jobs, just ask!</p>
  </header>

  <p class="label" style="top:368px">NAME</p>
  <p class="label" style="top:437px">TITLE</p>
  <p class="label" style="top:508px">PHONE</p>
  <p class="label" style="top:581px">WEBSITE</p>

  <p class="value value--on-green" style="left:559px;top:368px">DEREK OSSINGTON</p>
  <p class="value value--on-white" style="left:559px;top:440px">OWNER</p>
  <p class="value value--on-green" style="left:555px;top:512px">0000000</p>
  <p class="value value--web" style="left:550px;top:592px">WWW.HEDGEBUDDYCO.COM</p>
</main>
</body>
</html>
```